Briefkopf für Verwaltung im Taubertal
Zielgruppe
Die Verwaltungsgemeinschaft Wendelmark setzt sich aus den vier Kommunen zusammen: Stadt Wendelmark, Gemeinde Erlenbrunn, Gemeinde Hollerau und Gemeinde Kaltensee. Als kommunaler Ansprechpartner sprechen wir alle Bürgerinnen und Bürger an.
Aufgabenstellung
Das Logo der Verwaltungsgemeinschaft soll im Briefkopf abgebildet werden. Wesentliche Inhalte wie Adresse, Telefon, Mail, etc. sollen vorhanden sein. Der Briefkopf sollte nach Möglichkeit der DIN-Norm (DIN 5008) entsprechen und Falzmarken enthalten. Der Ausdruck erfolgt vorwiegend in Schwarz-Weiß, nur gelegentlich in Farbe. Daher soll der Briefkopf auch in Schwarz-Weiß Druck optisch ansprechbar wirken und zudem relativ wenig Tonerfarbe verbrauchen. Die Gestaltung soll sowohl neutral, seriös, als auch freundlich wirken.

```html
<!DOCTYPE html>
<html lang="de">
<head>
<meta charset="utf-8">
<title>Briefkopf Verwaltungsgemeinschaft Wendelmark</title>
<link href="https://fonts.googleapis.com/css2?family=Inter:wght@400;500&display=swap" rel="stylesheet">
<style>
  :root {
    --backdrop: #e4e4e4;
    --paper: #ffffff;
    --ink: #222222;
    --ink-soft: #333333;
    --frame: #333333;
    --accent: #b8302a;
    --divider: #a0705a;
  }
  * { margin: 0; padding: 0; box-sizing: border-box; }
  html, body {
    width: 862px; height: 1200px; overflow: hidden;
    background: var(--backdrop);
    font-family: "Inter", Arial, sans-serif;
    color: var(--ink);
  }
  .sheet {
    position: absolute; left: 37px; top: 43px;
    width: 787px; height: 1113px;
    background: var(--paper);
    border: 1px solid var(--frame);
  }
  .abs { position: absolute; }

  .brand-name {
    right: 227px; top: 60px;
    text-align: right; text-transform: uppercase;
    font-weight: 500; color: var(--ink);
    letter-spacing: 0.06em;
  }
  .brand-name .line1 { display: block; font-size: 15px; }
  .brand-name .line2 { display: block; font-size: 22px; margin-top: 2px; letter-spacing: 0.08em; }
  .brand-square {
    left: 582px; top: 60px; width: 46px; height: 46px;
    background: var(--accent);
  }

  .return-address {
    left: 83px; top: 178px; width: 300px;
    font-size: 8.5px; text-align: center;
    padding-bottom: 2px; border-bottom: 0.8px solid var(--ink);
  }

  .sender {
    left: 577px; top: 176px; height: 164px;
    border-left: 1px solid var(--divider);
    padding-left: 8px;
    font-size: 11px; line-height: 14.5px; color: var(--ink-soft);
  }
  .sender .title { font-weight: 500; color: var(--ink); margin-top: 7px; }
  .sender p + p { margin-top: 7px; }
  .sender .date { margin-top: 19px; }

  .window-dot { width: 1.5px; height: 1.5px; background: var(--ink); top: 345px; }

  .fold-mark { left: 11px; width: 16px; height: 1px; background: var(--ink); }

  .reference-row { top: 403px; font-size: 8.5px; color: var(--ink-soft); }

  .footer-col {
    top: 1048px; height: 49px;
    border-left: 1px solid var(--accent);
    padding-left: 7px;
    font-size: 8.3px; line-height: 10.3px; color: var(--ink-soft);
  }
  .footer-col h3 { font-size: 8.5px; font-weight: 500; color: var(--ink); }
  .bank-second { top: 1048px; font-size: 8.3px; line-height: 10.3px; color: var(--ink-soft); padding-top: 10.3px; }
</style>
</head>
<body>
<div class="sheet">
  <div class="abs brand-name">
    <span class="line1">Verwaltungsgemeinschaft</span>
    <span class="line2">Wendelmark</span>
  </div>
  <div class="abs brand-square"></div>

  <div class="abs return-address">VGem Wendelmark · Lindenplatz 4 · 97390 Wendelmark</div>

  <div class="abs sender">
    <p class="title">Körperschaft<br>des öffentlichen Rechts</p>
    <p>Lindenplatz 4<br>97390 Wendelmark</p>
    <p>Tel. 0 93 41 / 56 10-0<br>Fax 0 93 41 / 56 10-49<br>E-Mail: info@wendelmark.de</p>
    <p class="date">Wendelmark, den</p>
  </div>

  <div class="abs window-dot" style="left:75px"></div>
  <div class="abs window-dot" style="left:393px"></div>

  <div class="abs fold-mark" style="top:392px"></div>
  <div class="abs fold-mark" style="top:555px"></div>

  <div class="abs reference-row" style="left:69px">Unser Zeichen:</div>
  <div class="abs reference-row" style="left:244px">Ihnen schreibt:</div>
  <div class="abs reference-row" style="left:415px">Tel.-Durchwahl:</div>
  <div class="abs reference-row" style="left:586px">E-Mail:</div>

  <div class="abs footer-col" style="left:39px">
    <h3>Mitgliedsgemeinden:</h3>
    Stadt Wendelmark, Gemeinde Erlenbrunn,<br>Gemeinde Hollerau,<br>Gemeinde Kaltensee
  </div>
  <div class="abs footer-col" style="left:241px">
    <h3>Homepages:</h3>
    www.wendelmark.de, www.erlenbrunn.de,<br>www.hollerau.de,<br>www.kaltensee.de
  </div>
  <div class="abs footer-col" style="left:447px">
    <h3>Bankverbindungen:</h3>
    Kreissparkasse Talgrund<br>IBAN: DE00 1234 5678 0000 1111 22<br>BIC: TALGDEX1XXX
  </div>
  <div class="abs bank-second" style="left:613px">
    Volksbank Auengau<br>IBAN: DE00 8765 4321 0000 3333 44<br>BIC: AUENDEX1XXX
  </div>
</div>
</body>
</html>
```